Revamp Marketing Website For Video Production Website

need to revamp current website www.quillmediareels.example
reference sites www.fentaclips.example & http://layoutnook.example/quill/
Use all current content on current quill website. I want a revamped modenr look. Sometbing that wows customers.
reference site www.fentaclips.example
Target Market(s)
business owners
Industry/Entity Type
Video Production
Number of Pages Required
5+ page
Colors
Designer to choose colors to be used in the design.
Requirements
Must have
- need to revamp current website www.quillmediareels.example
- reference sites www.fentaclips.example & http://layoutnook.example/quill/
- Use all current content on current quill website. I want a revamped modenr look. Sometbing that wows customers.
- reference site www.fentaclips.example
Nice to have
Should not have

```html
<!DOCTYPE html>
<html lang="en">
<head>
<meta charset="utf-8">
<title>Quill – Marketing Videos Made For You</title>
<link href="https://fonts.googleapis.com/css2?family=Poppins:wght@300;400;500;600;700&display=swap" rel="stylesheet">
<style>
  :root {
    --brand-blue: #0aa8e8;
    --ink: #161616;
    --body-grey: #4a4a4a;
    --white: #ffffff;
    --rule-blue: #3d86c0;
    --hero-top: #2b3438;
    --hero-mid: #5e6466;
    --hero-warm: #7a5a3a;
    --hero-ground: #1d130d;
  }
  * { box-sizing: border-box; margin: 0; padding: 0; }
  html, body { width: 1100px; height: 1200px; overflow: hidden; background: var(--white); }
  body { font-family: 'Poppins', sans-serif; position: relative; }

  .hero { position: absolute; left: 0; top: 0; width: 1100px; height: 618px; overflow: hidden; }
  .hero-photo {
    position: absolute; inset: 0;
    background: linear-gradient(180deg, var(--hero-top) 0%, var(--hero-mid) 40%, var(--hero-warm) 68%, var(--hero-ground) 100%);
  }

  .nav { position: absolute; left: 0; top: 0; width: 1100px; height: 76px; }
  .logo { position: absolute; left: 75px; top: 22px; display: flex; align-items: center; gap: 8px; }
  .logo-mark { width: 14px; height: 14px; background: var(--brand-blue); }
  .logo-name { font-size: 24px; font-weight: 700; color: var(--white); letter-spacing: 2px; line-height: 1; }
  .logo-tag { position: absolute; left: 75px; top: 49px; font-size: 7px; font-weight: 500; color: #ddd; letter-spacing: .6px; }
  .nav-links { position: absolute; left: 275px; top: 29px; display: flex; gap: 27px; list-style: none; }
  .nav-links li { font-size: 13px; font-weight: 500; color: var(--white); }
  .login { position: absolute; left: 901px; top: 29px; font-size: 13px; font-weight: 500; color: var(--white); }
  .signup { position: absolute; left: 959px; top: 21px; width: 93px; height: 36px; border: 2px solid var(--brand-blue); border-radius: 2px; color: var(--brand-blue); font-size: 13px; font-weight: 500; display: flex; align-items: center; justify-content: center; }

  .hero-title { position: absolute; left: 0; width: 1100px; top: 168px; text-align: center; font-size: 51px; font-weight: 500; color: var(--white); }
  .hero-sub { position: absolute; left: 0; width: 1100px; top: 244px; text-align: center; font-size: 24px; font-weight: 400; color: var(--white); }
  .hero-rule { position: absolute; top: 260px; width: 187px; height: 3px; background: var(--white); }
  .cta { position: absolute; left: 411px; top: 302px; width: 269px; height: 56px; background: var(--brand-blue); color: var(--white); font-size: 13px; font-weight: 600; display: flex; align-items: center; justify-content: center; border-radius: 2px; }
  .cta-note { position: absolute; left: 0; width: 1100px; top: 363px; text-align: center; font-size: 11px; color: var(--white); }
  .slide-dot { position: absolute; left: 538px; top: 599px; width: 27px; height: 3px; background: var(--white); }

  .promote { position: absolute; left: 0; top: 666px; width: 1100px; text-align: center; }
  .promote h2 { font-size: 48px; font-weight: 500; color: var(--brand-blue); line-height: 1.2; }
  .promote-sub { position: relative; margin-top: 8px; height: 36px; }
  .promote-sub span { font-size: 25px; color: var(--brand-blue); }
  .promote-rule { position: absolute; top: 20px; height: 3px; background: var(--ink); }
  .promote p { margin: 22px auto 0; width: 940px; font-size: 16px; font-weight: 300; color: var(--body-grey); line-height: 1.5; }

  .create { position: absolute; left: 88px; top: 962px; }
  .create-line { font-size: 26px; font-weight: 600; line-height: 46px; color: var(--ink); }
  .create-line.accent { color: var(--brand-blue); font-weight: 700; }

  .networks { position: absolute; left: 567px; top: 982px; width: 455px; height: 160px; }
  .networks-v { position: absolute; left: 0; top: 0; width: 3px; height: 160px; background: var(--rule-blue); }
  .networks-h { position: absolute; left: 2px; top: 79px; width: 453px; height: 3px; background: var(--rule-blue); }
  .network { position: absolute; width: 90px; display: flex; flex-direction: column; align-items: center; gap: 4px; font-size: 12px; font-weight: 500; color: var(--ink); }
  .network-dot { width: 10px; height: 10px; border-radius: 50%; background: var(--brand-blue); }
</style>
</head>
<body>
  <header class="hero">
    <div class="hero-photo" role="img" aria-label="Photo of a group of friends jumping on a beach at sunset, silhouetted against the sun"></div>

    <nav class="nav">
      <div class="logo"><span class="logo-mark"></span><span class="logo-name">QUILL</span></div>
      <div class="logo-tag">MARKETING VIDEOS MADE FOR YOU</div>
      <ul class="nav-links">
        <li>Home</li><li>How It Works</li><li>Examples</li><li>FAQ</li><li>Contact Us</li><li>Pricing</li>
      </ul>
      <span class="login">Log In</span>
      <span class="signup">Sign Up</span>
    </nav>

    <h1 class="hero-title">Attention Grabbing Video Ads</h1>
    <span class="hero-rule" style="left:202px"></span>
    <span class="hero-rule" style="left:711px"></span>
    <div class="hero-sub">Delivered in 24 Hours!</div>
    <div class="cta">Get One Free Video Mock Up Now!</div>
    <div class="cta-note">No Purchase Necessary</div>
    <span class="slide-dot"></span>
  </header>

  <section class="promote">
    <h2>Promote Anything</h2>
    <div class="promote-sub">
      <span class="promote-rule" style="left:337px;width:60px"></span>
      <span>Anywhere in the Web</span>
      <span class="promote-rule" style="left:696px;width:66px"></span>
    </div>
    <p>For less than the cost and time of a DIY video maker software, we will make you world class promotional marketing videos that will make your business stand out from the competition.</p>
  </section>

  <section class="create">
    <div class="create-line accent">We Create</div>
    <div class="create-line">Award Winning Promotional</div>
    <div class="create-line accent">Marketing Videos</div>
    <div class="create-line">To Use All Over The Web</div>
  </section>

  <section class="networks" aria-label="Platforms we create for">
    <span class="networks-v"></span>
    <span class="networks-h"></span>
    <div class="network" style="left:31px;top:22px"><span class="network-dot"></span>Facely</div>
    <div class="network" style="left:124px;top:22px"><span class="network-dot"></span>Pictora</div>
    <div class="network" style="left:217px;top:22px"><span class="network-dot"></span>Circlr</div>
    <div class="network" style="left:310px;top:22px"><span class="network-dot"></span>Streamo</div>
    <div class="network" style="left:31px;top:104px"><span class="network-dot"></span>Reelio</div>
    <div class="network" style="left:124px;top:104px"><span class="network-dot"></span>Workly</div>
    <div class="network" style="left:217px;top:104px"><span class="network-dot"></span>Pinnacly</div>
    <div class="network" style="left:310px;top:104px"><span class="network-dot"></span>Chirply</div>
  </section>
</body>
</html>
```